TrueGrindz Complete Stationery - Logo already designed

I already have the logo designed see attached. I need have a full set of stationary and business card designed for printing. I have attached an example of what I mean.

Please feel free to be creative. Also you can use the X in the logo by its self if you think it will work.

My details:

Name: Corwin Lestak
Social media handles: @corwinlestak
W: corwinlestak.com
E: info@corwinlestak.com
​P: 08 7493 5286
PO Box 7382, Kelvale 6027
ABN 83 402 719 265

Target Market(s)

Anyone looking to be inspired.

Industry/Entity Type

Business

Font styles to use
Sans Serif

Colors
fbee3e
000000

Requirements
Must have
• My details:
• Name: Corwin Lestak
• Social media handles: @corwinlestak
• W: corwinlestak.com
• E: info@corwinlestak.com
• ​P: 08 7493 5286
• PO Box 7382, Kelvale 6027
• ABN 83 402 719 265
Nice to have
• Something a little different
Should not have
• must not look tacky.

```html
<!DOCTYPE html>
<html lang="en">
<head>
<meta charset="utf-8">
<title>TrueGrindz Business Card</title>
<link rel="stylesheet" href="https://fonts.googleapis.com/css2?family=Open+Sans:ital,wght@0,400;0,600;0,800;1,400&display=swap">
<style>
  :root {
    --brand-yellow: #fbee3e;
    --brand-gold: #f2c21b;
    --ink: #000000;
    --card-black: #0b0b0b;
    --paper: #ffffff;
    --text-dark: #1a1a1a;
    --backdrop: #d9d6d2;
  }
  * { margin: 0; padding: 0; box-sizing: border-box; }
  html, body {
    width: 1200px; height: 1200px; overflow: hidden;
    background: var(--backdrop);
    font-family: "Open Sans", sans-serif;
  }
  .sheet {
    width: 1200px; height: 1200px;
    display: flex; flex-direction: column; align-items: center; justify-content: center;
    gap: 80px;
  }
  .card {
    position: relative;
    width: 760px; height: 464px;
    box-shadow: 0 10px 28px rgba(0,0,0,0.25);
  }
  .card--front { background: var(--card-black); }
  .card--back { background: var(--paper); }

  .wordmark {
    display: flex; align-items: center; gap: 14px;
    font-weight: 800; letter-spacing: -1px; line-height: 1;
  }
  .wordmark__dot { width: 18px; height: 18px; border-radius: 50%; background: var(--brand-gold); }

  .card--front .wordmark {
    position: absolute; left: 50%; top: 44%;
    transform: translate(-50%, -50%);
    color: var(--paper); font-size: 76px;
  }
  .social {
    position: absolute; left: 218px; top: 318px;
    font-size: 15px; color: var(--paper);
  }
  .social__label { color: var(--brand-gold); }

  .card--back .wordmark {
    position: absolute; right: 64px; top: 150px;
    color: var(--ink); font-size: 54px;
  }
  .contact {
    position: absolute; left: 60px; top: 150px;
    color: var(--text-dark); font-size: 15px; line-height: 1.45;
  }
  .contact__name { font-size: 21px; font-weight: 600; line-height: 1.2; }
  .contact__role { font-style: italic; margin-bottom: 12px; }
  .contact__details { margin-bottom: 12px; }
  .contact__line { display: flex; align-items: center; gap: 9px; }
  .contact__line svg { width: 13px; height: 13px; flex: none; }
</style>
</head>
<body>
<main class="sheet">
  <section class="card card--front">
    <div class="wordmark"><span class="wordmark__dot"></span>TrueGrindz</div>
    <p class="social"><span class="social__label">Social media:</span> @corwinlestak</p>
  </section>

  <section class="card card--back">
    <div class="contact">
      <p class="contact__name">Corwin Lestak</p>
      <p class="contact__role">Director</p>
      <div class="contact__details">
        <p>ABN 83 402 719 265</p>
        <p>PO Box 7382, Kelvale 6027</p>
      </div>
      <p class="contact__line">
        <svg viewBox="0 0 16 16"><path fill="#1a1a1a" d="M4 1l3 3-1.6 1.8c.8 1.9 2.1 3.2 4 4L11.2 8.2 14.5 11 13 14c-6.5 0-11-4.5-11-11z"/></svg>
        08 7493 5286
      </p>
      <p class="contact__line">
        <svg viewBox="0 0 16 16"><rect x="1" y="3" width="14" height="10" fill="#1a1a1a"/><path d="M1.5 3.5L8 9l6.5-5.5" fill="none" stroke="#fff" stroke-width="1.2"/></svg>
        info@corwinlestak.com
      </p>
      <p class="contact__line">
        <svg viewBox="0 0 16 16" fill="none" stroke="#1a1a1a" stroke-width="1.3"><circle cx="8" cy="8" r="6.5"/><ellipse cx="8" cy="8" rx="2.8" ry="6.5"/><path d="M1.5 8h13"/></svg>
        www.corwinlestak.com
      </p>
    </div>
    <div class="wordmark"><span class="wordmark__dot"></span>TrueGrindz</div>
  </section>
</main>
</body>
</html>
```